Optical Finish Examiner Commercial Brochure

Match the design of this "OFE - datasheet" powerpoint brochure with the website and add a touch of modernity to sell this new and very innovative product. Keep the Powerpoint format and the text in French. Use the HTML version to translate with Chrome into your language.
https://norvik-works.example/media_clips/optical-finish-examiner/
Please note that the V1.5 presentation is only an example of a powerpoint presentation made, it is the Datasheet that must be redesigned.

Target Market(s)

The industry manufacturing metal parts, watches, automobiles, refurbished mobiles

Industry/Entity Type

Horlogerie, Automobile, Mobile, médical

Font styles to use
Sans Serif

Colors
0054AA
0677BA
7BADD7
CADEEF
E8F1F8

Requirements
Must have
• A very modern design
Nice to have
• Fine lines of lightness
Should not have
• too many colors

```html
<!DOCTYPE html>
<html lang="fr">
<head>
<meta charset="utf-8">
<title>Optical Finish Examiner – fiche produit</title>
<link href="https://fonts.googleapis.com/css2?family=Aldrich&family=Nunito+Sans:wght@400;600;700;800&display=swap" rel="stylesheet">
<style>
:root{
  --navy:#1b2131;
  --blue:#0677BA;
  --blue-deep:#0054AA;
  --sky:#7BADD7;
  --mist:#CADEEF;
  --ice:#E8F1F8;
  --stage:#6e6f73;
  --ink:#3b3f48;
  --white:#ffffff;
}
*{margin:0;padding:0;box-sizing:border-box}
html,body{width:1200px;height:834px;overflow:hidden;background:var(--stage)}
body{position:relative;font-family:"Nunito Sans",sans-serif;color:var(--ink)}
.page{position:absolute;top:88px;width:466px;height:658px;background:var(--white);overflow:hidden;box-shadow:0 3px 10px rgba(0,0,0,.25)}
.page--front{left:105px}
.page--back{left:635px}
.abs{position:absolute}
.display{font-family:"Aldrich",sans-serif;text-transform:uppercase;letter-spacing:.5px;line-height:1.05;font-weight:400}
.body{font-size:6px;line-height:1.36;text-align:justify}
.body p+p{margin-top:5px}
.photo{position:absolute}
/* front */
.hero-title{left:18px;top:118px;font-size:16px;color:var(--white)}
.hero-sub{left:16px;top:167px;font-size:7.2px;font-weight:800;color:var(--white);line-height:1.7;text-transform:uppercase}
.quality{left:0;top:228px;width:466px;height:151px;background:var(--navy);color:#e6e9ef}
.quality h2{position:absolute;left:18px;top:18px;font-size:11.5px;color:var(--white)}
.quality .body{position:absolute;left:18px;top:56px;width:214px;color:#d8dce4}
.questions{position:absolute;left:242px;top:16px;width:210px;list-style:none}
.questions li{font-size:6px;line-height:1.32;color:#d8dce4;padding-left:10px;position:relative;margin-bottom:5px;text-align:justify}
.questions li::before{content:"";position:absolute;left:0;top:1px;width:5px;height:5px;border:1px solid var(--sky);border-radius:50%}
.supprimer{left:18px;top:394px;width:215px}
.supprimer h2{font-size:11.5px;color:var(--navy)}
.supprimer .body{margin-top:10px}
.benefits{left:243px;top:379px;width:223px;height:279px;background:var(--blue)}
.benefits h2{position:absolute;left:14px;top:15px;font-size:12px;color:var(--white)}
.benefits ul{position:absolute;left:14px;top:47px;width:195px;list-style:none}
.benefits li{font-size:6.1px;line-height:1.3;color:var(--white);padding-left:12px;position:relative;margin-bottom:8px}
.benefits li svg{position:absolute;left:0;top:0}
.quote{left:18px;width:215px;display:flex;align-items:center;gap:10px;border-top:1px solid #d6d9de;padding-top:6px}
.quote .mark{width:72px;font-size:5.6px;font-weight:800;color:var(--navy);text-transform:uppercase;line-height:1.2;display:flex;align-items:center;gap:4px}
.quote .mark i{display:inline-block;width:7px;height:7px;background:var(--blue);flex:none}
.quote p{flex:1;font-size:5.6px;font-style:italic;color:#6d727c;line-height:1.3}
/* back */
.sens{left:16px;top:121px;font-size:11.5px;color:var(--navy)}
.sens-text{left:16px;top:154px;width:272px}
.sens-text2{left:16px;top:200px;width:350px}
.tablet{position:absolute;top:234px;height:130px;background:#dfe3e8;border-radius:9px;padding:5px;box-shadow:0 2px 4px rgba(0,0,0,.25);z-index:2}
.tablet .screen{width:100%;height:100%;border-radius:4px}
.tag{position:absolute;height:19px;background:var(--blue);color:var(--white);font-size:7.4px;font-weight:800;text-transform:uppercase;display:flex;align-items:center;padding:0 10px;z-index:3}
.col-blue{left:0;top:240px;width:224px;height:418px;background:var(--blue)}
.col-blue h2{position:absolute;left:16px;top:144px;font-size:11.5px;color:var(--white)}
.col-blue .body{position:absolute;left:16px;top:177px;width:200px;color:var(--white)}
.divider{left:224px;top:360px;width:6px;height:298px;background:var(--mist)}
.col-white{left:245px;top:384px;width:208px}
.col-white h2{font-size:11.5px;color:var(--navy)}
.col-white .body{margin-top:9px}
.contact{position:absolute;left:16px;top:604px;list-style:none}
.contact li{display:flex;align-items:center;gap:6px;font-size:6px;color:var(--white);margin-bottom:5px}
.contact svg{flex:none}
.brand{position:absolute;left:168px;top:614px;width:58px;display:flex;flex-direction:column;align-items:center;gap:3px;font-family:"Aldrich",sans-serif;font-size:8px;color:var(--blue-deep);letter-spacing:.4px;white-space:nowrap}
.brand i{width:7px;height:7px;background:var(--blue-deep);display:block}
</style>
</head>
<body>

<!-- ========== FRONT PAGE ========== -->
<section class="page page--front">
  <svg class="abs" style="left:0;top:0" width="466" height="228" viewBox="0 0 466 228">
    <rect width="466" height="228" fill="#1b2131"/>
    <defs><linearGradient id="g1" x1="0" y1="0" x2="1" y2="1"><stop offset="0" stop-color="#9a9ea5"/><stop offset=".6" stop-color="#5d6169"/><stop offset="1" stop-color="#2e3139"/></linearGradient></defs>
    <polygon points="200,0 466,0 466,228 90,228" fill="url(#g1)"/>
    <polygon points="0,0 60,0 210,130 0,130" fill="#0677BA"/>
    <polygon points="0,95 250,95 300,0 345,0 228,228 0,228" fill="#0677BA"/>
    <polygon points="0,0 40,0 0,30" fill="#0054AA"/>
    <polygon points="22,18 62,18 143,90 110,90" fill="#ffffff"/>
  </svg>
  <div class="photo" role="img" aria-label="Horloger contrôlant un composant à la loupe binoculaire" style="left:220px;top:0;width:246px;height:228px"></div>
  <h1 class="abs display hero-title">Optical Finish<br>Examiner</h1>
  <p class="abs hero-sub">La réalité virtuelle au service d’une<br>méthodologie pour un contrôle esthétique<br>&nbsp;horloger maîtrisé</p>

  <div class="abs quality">
    <h2 class="display">Maîtriser la qualité<br>du contrôle esthétique</h2>
    <div class="body">
      <p>Associé au concept de qualité « perçue », le contrôle esthétique est largement présent dans l’industrie horlogère dont les produits ont vocation à répondre à des qualités autant techniques qu’esthétiques. La perception d’un aspect irréprochable est souvent perçue comme le gage d’une qualité technique irréprochable.</p>
      <p>Alors que les coûts opérationnels, les investissements et l’impact « client » de ce type de contrôle sont très importants, les résultats obtenus sont variables d’un contrôleur à l’autre. Ces résultats s’appuient essentiellement sur des notions subjectives qu’il est difficile de partager, de transmettre et de capitaliser.</p>
    </div>
    <ul class="questions">
      <li>Comment adopter un langage et une compréhension communes de la qualité esthétique au niveau de l’entreprise étendue à ses clients et ses fournisseurs, et ceci de façon simple et univoque ?</li>
      <li>Comment évaluer et exprimer de façon tangible, de manière fiable et durable (répétable et reproductible) la qualité esthétique d’un composant horloger ?</li>
      <li>Comment former (et évaluer) de manière homogène les compétences opérationnelles des personnes en charge du contrôle esthétique ?</li>
      <li>Comment sur la base d’une échelle sémantique (rayes, marques, déformations, taches, ...) concevoir des séquences pédagogiques réalistes et attrayantes pour enseigner et diffuser plus largement la pratique du contrôle esthétique ?</li>
    </ul>
  </div>

  <div class="abs supprimer">
    <h2 class="display">Supprimer la gestion des composants physiques utilisés pour la formation</h2>
    <div class="body">
      <p>Les entreprises horlogères doivent gérer et entretenir des jeux de composants physiques pour la formation des personnes en charge du contrôle esthétique. Même si peu de composants sont concernés par ce contrôle, la simple combinatoire des différents matériaux sur les différents modèles se traduit par une charge importante. Il faut y ajouter le renouvellement régulier des jeux de composants (modèles existants et nouveaux modèles) et leur distribution sur les sites concernés par le contrôle visuel (les concessionnaires et distributeurs en charge du SAV notamment).</p>
      <p>En numérisant complètement les composants concernés (3D, texture, éclairage, ...) et en donnant la possibilité d’insérer les différents défauts esthétiques le OFE permet de supprimer la charge de gestion précédente.</p>
    </div>
  </div>
  <div class="abs quote" style="top:584px">
    <div class="mark"><i></i>Atelier Lémanique</div>
    <p>Avec OFE, nous pouvons désormais former des contrôleurs horlogers avec un outil moderne qui permet de tracer les progrès et de gérer le R&amp;R» - ATELIER LÉMANIQUE</p>
  </div>
  <div class="abs quote" style="top:622px">
    <div class="mark"><i></i>École Horlogère</div>
    <p>Grâce à OFE, nous avons une adhésion totale des étudiants en horlogerie à la démarche de contrôle esthétique» - École Horlogère du Léman</p>
  </div>

  <div class="abs benefits">
    <h2 class="display">OFE permet :</h2>
    <ul>
      <li><svg width="8" height="8" viewBox="0 0 8 8"><rect x=".5" y=".5" width="7" height="7" rx="1.5" fill="none" stroke="#fff" stroke-width=".8"/><path d="M2 4l1.4 1.4L6.3 2" fill="none" stroke="#fff" stroke-width=".9"/></svg>De supprimer la gestion des composants horlogers utilisés pour la formation des contrôleurs esthétiques</li>
      <li><svg width="8" height="8" viewBox="0 0 8 8"><rect x=".5" y=".5" width="7" height="7" rx="1.5" fill="none" stroke="#fff" stroke-width=".8"/><path d="M2 4l1.4 1.4L6.3 2" fill="none" stroke="#fff" stroke-width=".9"/></svg>Sensibiliser les collaborateurs au contrôle esthétique</li>
      <li><svg width="8" height="8" viewBox="0 0 8 8"><rect x=".5" y=".5" width="7" height="7" rx="1.5" fill="none" stroke="#fff" stroke-width=".8"/><path d="M2 4l1.4 1.4L6.3 2" fill="none" stroke="#fff" stroke-width=".9"/></svg>Accélérer les retours du Service après-vente et améliorer leur qualité</li>
      <li><svg width="8" height="8" viewBox="0 0 8 8"><rect x=".5" y=".5" width="7" height="7" rx="1.5" fill="none" stroke="#fff" stroke-width=".8"/><path d="M2 4l1.4 1.4L6.3 2" fill="none" stroke="#fff" stroke-width=".9"/></svg>Améliorer la démarche qualité dans son ensemble en se positionnant aux points «clé» des processus «métier»</li>
    </ul>
    <svg class="abs" style="left:0;top:150px" width="223" height="129" viewBox="0 0 223 129" role="img" aria-label="Mains d'horloger manipulant un mouvement avec des brucelles">
      <defs><linearGradient id="g2" x1="0" y1="0" x2="1" y2="1"><stop offset="0" stop-color="#a3a7ae"/><stop offset="1" stop-color="#3b3e45"/></linearGradient></defs>
      <polygon points="0,48 70,48 120,0 223,0 223,129 0,129" fill="url(#g2)"/>
      <polygon points="0,48 70,48 40,77 0,77" fill="#ffffff"/>
      <polygon points="0,77 40,77 0,115" fill="#CADEEF"/>
    </svg>
  </div>
</section>

<!-- ========== BACK PAGE ========== -->
<section class="page page--back">
  <svg class="abs" style="left:0;top:0" width="466" height="300" viewBox="0 0 466 300">
    <defs><linearGradient id="g3" x1="0" y1="0" x2="1" y2="1"><stop offset="0" stop-color="#8d9198"/><stop offset=".5" stop-color="#6b6f76"/><stop offset="1" stop-color="#3a3d44"/></linearGradient></defs>
    <rect x="0" y="0" width="190" height="102" fill="#1b2131"/>
    <polygon points="0,0 70,0 70,102 0,102" fill="#0677BA"/>
    <polygon points="18,26 46,26 110,86 82,86" fill="#ffffff"/>
    <polygon points="0,0 30,0 0,25" fill="#0054AA"/>
    <polygon points="190,0 466,0 466,197 420,197 342,138 168,138 168,100 190,100" fill="#c9ccd1"/>
    <polygon points="194,0 466,0 466,188 424,188 346,129 194,129" fill="url(#g3)"/>
    <polygon points="410,188 466,188 466,240" fill="#1b2131"/>
  </svg>
  <div class="photo" role="img" aria-label="Horloger portant une loupe et inspectant une pièce" style="left:194px;top:0;width:272px;height:129px"></div>

  <h2 class="abs display sens">Sensibiliser au<br>contrôle esthétique</h2>
  <p class="abs body sens-text">Les défauts esthétiques relèvent souvent d’un manque d’attention lors de la manipulation des composants concernés que ce soit lors de la fabrication, de l’assemblage ou encore de la commercialisation. Il est parfois difficile pour les entreprises horlogères de sensibiliser le personnel en charge sur cet aspect.</p>
  <p class="abs body sens-text2">En présentant une plateforme virtuelle répertoriant les différents types de défauts esthétiques et leurs causes connues, il devient très simple de donner accès à des parcours pédagogiques et d’évaluer la sensibilité des collaborateurs en charge.</p>

  <div class="abs col-blue">
    <h2 class="display">Améliorer les retours<br>du service après-vente</h2>
    <div class="body">
      <p>Une gestion efficace du SAV est une problématique récurrente des maisons horlogères. Comment s’assurer que les devis proposés soient corrects, que les interventions réalisées soient adaptées ou encore que le personnel en charge soit formé correctement ? Ceci est particulièrement vrai pour le contrôle esthétique car le client demande que les défauts qu’il « voit » soient corrigés.</p>
      <p>En donnant accès à la plateforme OFE au personnel du réseau de SAV, il est possible d’avoir en « temps réel » une fiche des défauts esthétiques constatés lors du diagnostic. OFE propose une interface intuitive permettant d’indiquer les défauts avec leur degré d’intensité conformément à la nomenclature établie et partagée par l’ensemble du réseau de SAV. Cela permet selon les cas de valider la nature et le montant du devis d’intervention (remplacement, polissage, prise en compte de la garantie, prêt ...).</p>
    </div>
  </div>
  <svg class="abs" style="left:0;top:568px" width="224" height="90" viewBox="0 0 224 90">
    <polygon points="0,0 224,24 224,90 0,90" fill="#1b2131"/>
    <polygon points="138,90 224,8 224,90" fill="#ffffff"/>
  </svg>
  <ul class="contact">
    <li><svg width="8" height="8" viewBox="0 0 8 8"><rect width="8" height="8" rx="2" fill="#0677BA"/><path d="M2.3 1.8l1 .9-.5.7c.3.6.8 1.1 1.4 1.4l.7-.5.9 1-.7.8C3.5 6 2 4.5 1.7 2.5z" fill="#fff"/></svg>+41 22 000 41 18</li>
    <li><svg width="8" height="8" viewBox="0 0 8 8"><rect width="8" height="8" rx="2" fill="#0677BA"/><rect x="1.6" y="2.3" width="4.8" height="3.4" fill="none" stroke="#fff" stroke-width=".6"/><path d="M1.6 2.3L4 4.3l2.4-2" fill="none" stroke="#fff" stroke-width=".6"/></svg>lena@norvik-works.example | norvik-works.example</li>
    <li><svg width="8" height="8" viewBox="0 0 8 8"><rect width="8" height="8" rx="2" fill="#0677BA"/><path d="M4 6.6C2.6 5 2.2 4.1 2.2 3.4a1.8 1.8 0 013.6 0c0 .7-.4 1.6-1.8 3.2z" fill="#fff"/><circle cx="4" cy="3.4" r=".6" fill="#0677BA"/></svg>Rue des Tilleuls 12, 1200 Genève</li>
  </ul>
  <div class="brand"><i></i>NORVIK WORKS</div>

  <div class="abs divider"></div>

  <div class="tablet" style="left:17px;width:213px">
    <div class="screen" role="img" aria-label="Interface du simulateur : panneau de réglages et rendu 3D d'un boîtier de montre doré" style="background:linear-gradient(90deg,#1d4f86 0 28%,#0b0b0d 28%,#3a2a12 65%,#8a5a1c 80%,#1a130a)"></div>
  </div>
  <div class="tablet" style="left:238px;width:213px">
    <div class="screen" role="img" aria-label="Grille de l'échelle sémantique des défauts esthétiques" style="background:linear-gradient(180deg,#0c1e3a 0 10%,#1a6fc0 10% 16%,#0e2748 16%)"></div>
  </div>
  <div class="tag" style="left:170px;top:282px;width:150px">
    <svg class="abs" style="left:-9px;top:0" width="9" height="19" viewBox="0 0 9 19"><polygon points="9,0 0,9.5 9,19" fill="#0677BA"/></svg>
    Une échelle sémantique
  </div>
  <div class="tag" style="left:170px;top:314px;width:142px">
    Une interface intuitive ...
    <svg class="abs" style="right:-9px;top:0" width="9" height="19" viewBox="0 0 9 19"><polygon points="0,0 9,9.5 0,19" fill="#0677BA"/></svg>
  </div>

  <div class="abs col-white">
    <h2 class="display">Améliorer la<br>démarche qualité globale</h2>
    <div class="body">
      <p>Les maisons horlogères sont en général très impliquées dans une démarche qualité pro-active. La recherche de causalité lorsque des défauts récurrents sont constatés est l’une de ces problématiques. Alors que les aspects liés aux performances sont souvent mis en avant, le contrôle esthétique n’est en général pas intégré dans une démarche qualité globale.</p>
      <p>L’utilisation du OFE sur l’ensemble du cycle de vie du produit horloger (conception, fabrication, distribution, SAV), permet de constituer une base de données de défauts esthétiques au fil de la vie des produits. Il est alors possible d’établir des corrélations lorsque des défauts visuels récurrents sont constatés et d’en rechercher les causes (choix des matériaux, montage, manipulation erronée, utilisation non conforme, ...) afin de les corriger et d’optimiser les processus associés.</p>
    </div>
    <h2 class="display" style="margin-top:16px">Une échelle sémantique<br>des défauts esthétiques</h2>
    <div class="body">
      <p>OFE s’appuie sur une grille sémantique permettant de définir 5 niveaux de gravité pour chacun des 5 défauts esthétiques génériques : Rayes – Marques/coups – Déformations – Tâches/propreté – Uniformité/Identité du produit.</p>
    </div>
  </div>
</section>

</body>
</html>
```